Vitalquorra.com

I need a web design for a Online Wellness Center based in Chicago, IL and it's called "Vitalquorra" We provide Health risk assessment to individuals and interventions. Our portal has a Health Activity tracker where our members record health activities and aerobic miles and biometric data. Our Online wellness center tracks the participant's progress toward health goals and awards points for completed activities.
I started working on this website but the designer was not able to designer a website which describes what we do. I need a fresh look on this project. I need a very attractive, responsive website which says what we do.
These are the things we do.
1. We provide Health Risk Assessments to individuals and Co-operations
2. We Provide Free health screenings to undeserved communities
3. Assist individuals access free or affordable medications
4. We ask providers/doctors to see (or do a complete physical) one individual free of charge once a year (those individuals who are no insured and don't have money to pay from their pocket)
5. Assist patient access lab work at low cost
Our goal is to provide services that will lower the cost of care for our members.

Here is the website: www.vitalquorra.com still underdevelopment. PLEASE DO NOT COPY THIS STYLE OF WEBSITE. IT'S A BAD DESIGN AND THAT IS WHY I'M RE-DESIGNING THE SITE

Target Market(s)

Health individuals between the age of 21 to 65 Plus years old. Insured and uninsured

Industry/Entity Type

Health And Wellness

Coding

Coded - Design and coding required

Number of Pages Required

5+ page

Colors
0292cd

Requirements
Must have
• I'm still working on this websiteHere is the menu: Home, About us, Services, Health Screening, Providers, Contacts
• Please see. www.vitalquorra.com
Nice to have
• Event calender
• Upcoming Event
• Medication
• Lab assist
• Providers/Free Clinics

```html
<!DOCTYPE html>
<html lang="en">
<head>
<meta charset="utf-8">
<title>Vitalquorra – Online Wellness Center</title>
<link rel="stylesheet" href="https://fonts.googleapis.com/css2?family=Open+Sans:wght@400;600;700;800&display=swap">
<style>
:root{
  --blue:#1a7fd0;
  --blue-bright:#0292cd;
  --navy:#1c3d8f;
  --navy-deep:#15306f;
  --green:#7cc242;
  --green-dark:#5fa52b;
  --ink:#333a44;
  --muted:#7a838e;
  --line:#e3e7ec;
  --soft:#f1f3f6;
  --white:#ffffff;
}
*{box-sizing:border-box;margin:0;padding:0}
html,body{width:1200px;height:2708px;overflow:hidden}
body{font-family:"Open Sans",Arial,sans-serif;color:var(--ink);background:var(--white);position:relative}
.wrap{width:1100px;margin:0 auto;position:relative}

/* top bar */
.topbar{height:40px;border-bottom:1px solid var(--line);font-size:14px;color:var(--blue)}
.topbar .wrap{display:flex;align-items:center;height:40px;gap:26px}
.topbar .item{display:flex;align-items:center;gap:7px}
.topbar .auth{margin-left:auto;display:flex;gap:8px}
.btn-sm{font-size:13px;font-weight:600;color:#fff;padding:5px 16px;border-radius:2px}
.btn-sm.login{background:var(--navy)}
.btn-sm.signup{background:var(--green)}

/* header */
.header{height:120px}
.header .wrap{display:flex;align-items:center;height:120px}
.brand{display:flex;align-items:center;gap:10px;font-size:38px;font-weight:700;color:var(--blue);letter-spacing:-.5px}
.brand .dot{width:34px;height:34px;border-radius:50%;background:var(--green)}
.nav{margin-left:auto;display:flex;gap:6px;font-size:15px;font-weight:600}
.nav a{color:var(--ink);text-decoration:none;padding:12px 16px}
.nav a.active{border-top:3px solid var(--blue);color:var(--blue);background:var(--soft)}

/* hero */
.hero{height:440px;position:relative;background:linear-gradient(110deg,#dfe9f2 0%,#c4d8ea 40%,#aac6df 70%,#8fb2d3 100%)}
.hero .arrow{position:absolute;top:190px;width:44px;height:44px;border-radius:50%;background:rgba(255,255,255,.65);display:flex;align-items:center;justify-content:center}
.hero .arrow.left{left:30px}.hero .arrow.right{right:30px}

/* info panels */
.panels{display:flex;height:320px}
.panel{flex:1;color:#fff;padding:26px 34px;text-align:center;position:relative}
.panel.blue{background:var(--blue)}
.panel.green{background:var(--green)}
.panel.navy{background:var(--navy)}
.panel .icon{width:40px;height:40px;margin:0 auto 8px;display:block}
.panel h3{font-size:20px;font-weight:700;margin-bottom:12px;letter-spacing:.3px}
.panel p{font-size:13px;line-height:1.6;opacity:.95}
.panel .more{display:inline-block;margin-top:16px;font-size:12px;font-weight:600;border:1px solid #fff;padding:6px 16px}
.hours{margin-top:14px;font-size:13px;text-align:left}
.hours div{display:flex;justify-content:space-between;padding:9px 6px;border-top:1px solid rgba(255,255,255,.45)}
.loc h4{font-size:14px;font-weight:700;margin-top:6px}
.loc p{font-size:13px;line-height:1.5}

/* services */
.services{height:280px;background:linear-gradient(180deg,#5d8fc4 0%,#3e73b1 100%);display:flex;justify-content:center;gap:22px;padding-top:40px}
.svc{width:226px;height:200px;background:var(--navy);color:#fff;text-align:center}
.svc .top{height:90px;display:flex;align-items:center;justify-content:center}
.svc h4{font-size:17px;font-weight:700;margin:8px 0 6px}
.svc p{font-size:12px;line-height:1.5;padding:0 18px;opacity:.9}

/* benefits */
.benefits{height:480px;position:relative}
.benefits .copy{position:absolute;left:50px;top:40px;width:560px}
.benefits h2{font-size:26px;font-weight:700;color:var(--ink);letter-spacing:.2px}
.benefits h2 span{color:var(--green)}
.benefits .rule{width:60px;height:3px;background:var(--blue);margin:10px 0 14px}
.benefits .lead{font-size:14px;line-height:1.6;color:var(--muted);margin-bottom:14px}
.ticks{list-style:none}
.ticks li{display:flex;gap:10px;font-size:13px;line-height:1.5;padding:6px 0;border-bottom:1px solid var(--line)}
.ticks svg{flex:none;margin-top:2px}
.btn{display:inline-block;background:var(--navy);color:#fff;font-size:14px;font-weight:600;padding:11px 24px;margin-top:18px}
.benefits .photo{position:absolute;right:0;top:30px;width:560px;height:430px;background:linear-gradient(100deg,#ffffff 0%,#e8eef5 30%,#c7d8ea 70%,#aac4de 100%)}

/* providers */
.providers{height:100px;background:var(--soft);margin-top:20px}
.providers .wrap{display:flex;align-items:center;height:100px}
.providers h2{font-size:26px;font-weight:700;color:var(--ink)}
.providers p{font-size:14px;color:var(--muted);margin-top:4px}
.providers .contact{margin-left:auto;display:flex;align-items:center;gap:10px;background:var(--navy);color:#fff;font-size:15px;font-weight:700;padding:14px 26px}

/* events */
.events{height:480px;padding-top:26px}
.events .wrap{display:flex;gap:60px}
.col-title{font-size:24px;font-weight:700;color:var(--blue);margin-bottom:20px}
.upcoming{width:560px}
.event{display:flex;gap:20px;margin-bottom:26px}
.event .thumb{flex:none;width:200px;height:150px;background:linear-gradient(135deg,#dfe8f1,#9fbcd8)}
.event h4{font-size:15px;font-weight:700;color:var(--blue)}
.event .date{font-size:12px;color:var(--muted);margin:4px 0 8px}
.event p{font-size:13px;line-height:1.55;color:var(--ink)}
.event .read{font-size:13px;font-weight:700;color:var(--ink);margin-top:8px;display:block}
.calendar{flex:1}
.cal{width:100%;border-collapse:collapse;font-size:13px;text-align:center}
.cal caption{font-size:22px;font-weight:600;padding:8px 0;background:var(--soft);caption-side:top;text-align:center}
.cal th{background:var(--navy);color:#fff;padding:8px 0;font-weight:600}
.cal td{border:1px solid var(--line);height:50px;vertical-align:top;text-align:right;padding:4px 6px;color:var(--ink)}
.cal td.off{color:#bbb}
.cal td.today{background:#fbeeb8}
.cal td.ev{background:#dbe9f7}

/* newsletter */
.newsletter{height:80px;background:var(--green);margin-top:10px}
.newsletter .wrap{display:flex;align-items:center;height:80px;color:#fff}
.newsletter h3{font-size:22px;font-weight:600;display:flex;align-items:center;gap:14px}
.newsletter form{margin-left:auto;display:flex}
.newsletter .field{width:260px;height:40px;background:#fff;color:var(--muted);font-size:13px;padding:11px 12px}
.newsletter .submit{height:40px;background:var(--navy-deep);color:#fff;font-size:13px;font-weight:700;padding:11px 20px}

/* footer */
.footer{height:260px;background:var(--navy);color:#fff}
.footer .wrap{display:flex;height:260px;align-items:center}
.fcol{flex:1;text-align:center}
.fcol svg{display:block;margin:0 auto 16px}
.fcol h5{font-size:16px;font-weight:700;margin-bottom:14px}
.fcol p{font-size:14px;line-height:1.6;opacity:.9}
.socials{display:flex;justify-content:center;gap:10px}
.socials span{width:26px;height:26px;border-radius:50%;background:rgba(255,255,255,.25)}
.bottom{height:68px;background:var(--navy-deep);color:#cdd6ea;text-align:center;font-size:13px;padding-top:14px}
.bottom nav{display:flex;justify-content:center;gap:20px;margin-bottom:6px;color:#fff}
</style>
</head>
<body>

<div class="topbar">
  <div class="wrap">
    <span class="item">
      <svg width="14" height="14" viewBox="0 0 24 24"><path fill="currentColor" d="M6.6 10.8a15 15 0 0 0 6.6 6.6l2.2-2.2a1 1 0 0 1 1-.25 11.4 11.4 0 0 0 3.6.57 1 1 0 0 1 1 1V20a1 1 0 0 1-1 1A17 17 0 0 1 3 4a1 1 0 0 1 1-1h3.5a1 1 0 0 1 1 1c0 1.25.2 2.45.57 3.57a1 1 0 0 1-.25 1z"/></svg>
      +1 773 555 0142</span>
    <span class="item">
      <svg width="15" height="12" viewBox="0 0 24 18"><rect x="1" y="1" width="22" height="16" fill="none" stroke="currentColor" stroke-width="2"/><path d="M1 1l11 9 11-9" fill="none" stroke="currentColor" stroke-width="2"/></svg>
      hello@vitalquorra.com</span>
    <div class="auth"><span class="btn-sm login">Login</span><span class="btn-sm signup">Signup</span></div>
  </div>
</div>

<header class="header">
  <div class="wrap">
    <div class="brand"><span class="dot"></span>Vitalquorra</div>
    <nav class="nav">
      <a class="active" href="#">Home</a><a href="#">About us</a><a href="#">Services</a><a href="#">Health Screening</a><a href="#">Providers</a><a href="#">Contacts</a>
    </nav>
  </div>
</header>

<section class="hero" role="img" aria-label="Photo of a smiling doctor and nurse in a bright clinic corridor">
  <span class="arrow left"><svg width="14" height="14" viewBox="0 0 14 14"><path d="M9 2L4 7l5 5" fill="none" stroke="#1c3d8f" stroke-width="2"/></svg></span>
  <span class="arrow right"><svg width="14" height="14" viewBox="0 0 14 14"><path d="M5 2l5 5-5 5" fill="none" stroke="#1c3d8f" stroke-width="2"/></svg></span>
</section>

<section class="panels">
  <div class="panel blue">
    <svg class="icon" viewBox="0 0 40 40"><path d="M6 20L20 8l14 12v14H24v-9h-8v9H6z" fill="#fff"/></svg>
    <h3>WELCOME OUR SITE</h3>
    <p>If you need a doctor for a health check, our online wellness center helps you find care, track progress and earn points for every healthy activity you complete with us.</p>
    <span class="more">READ MORE</span>
  </div>
  <div class="panel green">
    <svg class="icon" viewBox="0 0 40 40"><circle cx="20" cy="20" r="15" fill="none" stroke="#fff" stroke-width="3"/><path d="M20 11v10l7 4" fill="none" stroke="#fff" stroke-width="3"/></svg>
    <h3>OPENING HOURS</h3>
    <p>If you need a doctor, our team is ready to help during the hours below.</p>
    <div class="hours">
      <div><span>Monday – Friday</span><span>8.00 – 17.00</span></div>
      <div><span>Saturday</span><span>9.30 – 17.30</span></div>
      <div><span>Sunday</span><span>9.30 – 15.00</span></div>
    </div>
  </div>
  <div class="panel navy loc" style="background:var(--blue)">
    <svg class="icon" viewBox="0 0 40 40"><path d="M20 4a11 11 0 0 0-11 11c0 9 11 21 11 21s11-12 11-21A11 11 0 0 0 20 4z" fill="#fff"/><circle cx="20" cy="15" r="4" fill="#1a7fd0"/></svg>
    <h3>LOCATION PLAN</h3>
    <h4>ADDRESS :</h4>
    <p>Vitalquorra<br>1450 Larkwood Avenue,<br>Chicago, IL 60699 USA</p>
    <h4>TELEPHONE :</h4>
    <p>+1 773 555 0142</p>
    <h4>EMAIL :</h4>
    <p>hello@vitalquorra.com</p>
  </div>
</section>

<section class="services" role="img" aria-label="Soft blue photo backdrop of a medical team behind service tiles">
  <div class="svc">
    <div class="top"><svg width="56" height="50" viewBox="0 0 24 22"><path d="M12 21S1 14 1 7a5.5 5.5 0 0 1 11-1 5.5 5.5 0 0 1 11 1c0 7-11 14-11 14z" fill="#fff"/></svg></div>
    <h4>MEDICATION</h4><p>Help finding free or low cost medication for members who need it.</p>
  </div>
  <div class="svc">
    <div class="top"><svg width="46" height="54" viewBox="0 0 24 28"><path d="M8 2h8M9 2v9L2 25h20L15 11V2" fill="none" stroke="#fff" stroke-width="2.4"/><path d="M5 20h14l2 5H3z" fill="#fff"/></svg></div>
    <h4>LAB TEST</h4><p>Low cost lab work arranged with trusted partner labs nearby.</p>
  </div>
  <div class="svc">
    <div class="top"><svg width="52" height="54" viewBox="0 0 24 26"><path d="M5 2v8a5 5 0 0 0 10 0V2M10 15v4a5 5 0 0 0 10 0v-4" fill="none" stroke="#fff" stroke-width="2.2"/><circle cx="20" cy="13" r="2.6" fill="#fff"/></svg></div>
    <h4>HEALTH SCREENING</h4><p>Free health screenings held in underserved communities.</p>
  </div>
  <div class="svc">
    <div class="top"><svg width="58" height="48" viewBox="0 0 28 22"><rect x="1" y="1" width="26" height="16" rx="2" fill="none" stroke="#fff" stroke-width="2.2"/><path d="M9 21h10" stroke="#fff" stroke-width="2.2"/><path d="M10 9h8M14 5v8" stroke="#fff" stroke-width="2.2"/></svg></div>
    <h4>ONLINE HELP</h4><p>Track activity, miles and biometric data on our member portal.</p>
  </div>
</section>

<section class="benefits">
  <div class="copy">
    <h2>BENEFITS OF OUR <span>WELLNESS SERVICES</span></h2>
    <div class="rule"></div>
    <p class="lead">Our community is serving tirelessly to assure the health wellness services and choose the suitable plans for you. Here are the features:</p>
    <ul class="ticks">
      <li><svg width="16" height="16" viewBox="0 0 16 16"><circle cx="8" cy="8" r="8" fill="#7cc242"/><path d="M4 8l3 3 5-6" fill="none" stroke="#fff" stroke-width="2"/></svg>We provide Health Risk Assessments to individuals and Co-operations</li>
      <li><svg width="16" height="16" viewBox="0 0 16 16"><circle cx="8" cy="8" r="8" fill="#7cc242"/><path d="M4 8l3 3 5-6" fill="none" stroke="#fff" stroke-width="2"/></svg>We Provide Free health screenings to underserved communities</li>
      <li><svg width="16" height="16" viewBox="0 0 16 16"><circle cx="8" cy="8" r="8" fill="#7cc242"/><path d="M4 8l3 3 5-6" fill="none" stroke="#fff" stroke-width="2"/></svg>Assist individuals access free or affordable medications</li>
      <li><svg width="16" height="16" viewBox="0 0 16 16"><circle cx="8" cy="8" r="8" fill="#7cc242"/><path d="M4 8l3 3 5-6" fill="none" stroke="#fff" stroke-width="2"/></svg>We ask providers/doctors to see (or do a complete physical) one individual free of charge once a year, for those individuals who are not insured and don't have money to pay from their pocket</li>
      <li><svg width="16" height="16" viewBox="0 0 16 16"><circle cx="8" cy="8" r="8" fill="#7cc242"/><path d="M4 8l3 3 5-6" fill="none" stroke="#fff" stroke-width="2"/></svg>Assist patient access lab work at low cost. Our goal is to provide services that will lower the cost of care for our members</li>
    </ul>
    <span class="btn">Read More</span>
  </div>
  <div class="photo" role="img" aria-label="Photo of a smiling female doctor in front of her medical team"></div>
</section>

<section class="providers">
  <div class="wrap">
    <div>
      <h2>PROVIDERS/FREE CLINICS</h2>
      <p>If you need a doctor for a free check, find a clinic near you, consectetur adipiscing elit.</p>
    </div>
    <span class="contact">
      <svg width="18" height="18" viewBox="0 0 24 24"><path fill="#fff" d="M6.6 10.8a15 15 0 0 0 6.6 6.6l2.2-2.2a1 1 0 0 1 1-.25 11.4 11.4 0 0 0 3.6.57 1 1 0 0 1 1 1V20a1 1 0 0 1-1 1A17 17 0 0 1 3 4a1 1 0 0 1 1-1h3.5a1 1 0 0 1 1 1c0 1.25.2 2.45.57 3.57a1 1 0 0 1-.25 1z"/></svg>
      CONTACT WITH US</span>
  </div>
</section>

<section class="events">
  <div class="wrap">
    <div class="upcoming">
      <h3 class="col-title">Upcoming Event</h3>
      <div class="event">
        <div class="thumb" role="img" aria-label="Photo of a clinic waiting room"></div>
        <div>
          <h4>FREE HEALTH SCREENING DAY</h4>
          <div class="date">Nov 18, 2015 | 3 Comments</div>
          <p>Join our team for free blood pressure, glucose and weight checks. Walk in, meet local providers and learn which simple steps can lower your cost of care this year.</p>
          <span class="read">Read More</span>
        </div>
      </div>
      <div class="event">
        <div class="thumb" role="img" aria-label="Photo of a colourful children's play room"></div>
        <div>
          <h4>FAMILY WELLNESS WORKSHOP</h4>
          <div class="date">Nov 26, 2015 | 2 Comments</div>
          <p>A friendly afternoon on healthy meals, daily activity and tracking aerobic miles in the member portal. Bring the whole family and earn points for taking part.</p>
          <span class="read">Read More</span>
        </div>
      </div>
    </div>
    <div class="calendar">
      <h3 class="col-title">Event Calender</h3>
      <table class="cal">
        <caption>&#8249;&nbsp;&nbsp;September 2015&nbsp;&nbsp;&#8250;</caption>
        <tr><th>Sun</th><th>Mon</th><th>Tue</th><th>Wed</th><th>Thu</th><th>Fri</th><th>Sat</th></tr>
        <tr><td class="off">30</td><td class="off">31</td><td>1</td><td>2</td><td>3</td><td>4</td><td>5</td></tr>
        <tr><td>6</td><td>7</td><td>8</td><td class="ev">9</td><td>10</td><td>11</td><td>12</td></tr>
        <tr><td>13</td><td>14</td><td>15</td><td>16</td><td class="today">17</td><td>18</td><td>19</td></tr>
        <tr><td>20</td><td class="ev">21</td><td class="ev">22</td><td>23</td><td>24</td><td>25</td><td>26</td></tr>
        <tr><td>27</td><td>28</td><td>29</td><td>30</td><td class="off">1</td><td class="off">2</td><td class="off">3</td></tr>
      </table>
    </div>
  </div>
</section>

<section class="newsletter">
  <div class="wrap">
    <h3><svg width="26" height="20" viewBox="0 0 24 18"><rect x="1" y="1" width="22" height="16" fill="none" stroke="#fff" stroke-width="2"/><path d="M1 1l11 9 11-9" fill="none" stroke="#fff" stroke-width="2"/></svg>Subscribe To Our Newsletter</h3>
    <form><span class="field">Your Email Address</span><span class="submit">SUBMIT</span></form>
  </div>
</section>

<footer class="footer">
  <div class="wrap">
    <div class="fcol">
      <svg width="30" height="30" viewBox="0 0 24 24"><path fill="#fff" d="M6.6 10.8a15 15 0 0 0 6.6 6.6l2.2-2.2a1 1 0 0 1 1-.25 11.4 11.4 0 0 0 3.6.57 1 1 0 0 1 1 1V20a1 1 0 0 1-1 1A17 17 0 0 1 3 4a1 1 0 0 1 1-1h3.5a1 1 0 0 1 1 1c0 1.25.2 2.45.57 3.57a1 1 0 0 1-.25 1z"/></svg>
      <h5>Telephone</h5><p>+1 773 555 0142</p>
    </div>
    <div class="fcol">
      <svg width="32" height="24" viewBox="0 0 24 18"><rect x="1" y="1" width="22" height="16" fill="none" stroke="#fff" stroke-width="2"/><path d="M1 1l11 9 11-9" fill="none" stroke="#fff" stroke-width="2"/></svg>
      <h5>E-Mail Us</h5><p>hello@vitalquorra.com</p>
    </div>
    <div class="fcol">
      <svg width="30" height="30" viewBox="0 0 24 24"><circle cx="12" cy="8" r="4" fill="#fff"/><path d="M4 22a8 8 0 0 1 16 0z" fill="#fff"/></svg>
      <h5>Follow Us</h5>
      <div class="socials"><span></span><span></span><span></span><span></span><span></span></div>
    </div>
    <div class="fcol">
      <svg width="28" height="32" viewBox="0 0 24 28"><path d="M12 1a9 9 0 0 0-9 9c0 8 9 17 9 17s9-9 9-17a9 9 0 0 0-9-9z" fill="#fff"/><circle cx="12" cy="10" r="3.4" fill="#1c3d8f"/></svg>
      <h5>Address</h5><p>1450 Larkwood Avenue,<br>Chicago IL 60699 USA</p>
    </div>
  </div>
</footer>

<div class="bottom">
  <nav><span>Home</span><span>About us</span><span>Services</span><span>Health Screening</span><span>Providers</span><span>Contacts</span></nav>
  <div>Copyright © 2015 - All right reserved</div>
</div>

</body>
</html>
```